Lantern Square, Steady Course. (Website Design)

We are launching a new bipartisan civic movement: Lantern Square. Steady Course.
The mission is this: Americans deserve a government that is legally required to serve them honestly.
We are looking for a world-class website designer capable of creating an emotionally powerful, modern, cinematic landing page experience that feels larger than politics.
This is not a campaign website for a political party or candidate. We are not looking for a red, white, and blue page with stripes, or American flags, or stock footage of smiling people in a voting booth. We are looking for an emotional and cinematic experience through and through.
The visual direction should feel:
Historic
Hopeful
American
Emotional
Cinematic
Trustworthy
Timeless
The goal is to make visitors feel that they are witnessing the beginning of something important and want to be part of it in the end.
Primary Objective:
Inspire visitors to participate in a one-minute survey and cast their vote.
The survey itself is extremely short and takes approximately one minute to complete.
Everything on the page should ultimately guide visitors toward this action while creating enough curiosity, trust, emotional engagement, and excitement that they feel compelled to take part in the movement.
Audience:
The audience is ordinary Americans across the political spectrum: Democrats, Republicans, Independents.
The design should feel unifying and welcoming.
It should avoid looking partisan, ideological, activist, or government-issued.
Creative Freedom:
We are intentionally giving designers substantial creative freedom.
We are not looking for someone to simply arrange content into predefined sections.
Instead, we are looking for a designer who can think strategically about user experience and persuasion.
The ideal design is as minimal as possible, but you may always:
Use as many sections as you believe are necessary.
Use as many images as you believe are necessary.
Include storytelling elements.
Include data visualizations.
Include timelines.
Include videos.
Include animations.
Include or exclude sections as you see fit.
Reorganize the flow entirely.
We uploaded some files containing text and section suggestions. You don’t have to use them.
We also uploaded some images to convey the general feel we’re looking for.
We are much more interested in the effectiveness of the overall experience than in any specific layout.
What success looks like:
Think outside the box.
Please do not create another generic political website. We have already explored those approaches.
We are looking for something different.
The winning design will be the one that most effectively guides visitors from curiosity to belief to participation.
When a visitor reaches the end of the experience, they should feel:
This is bigger than politics.
This is something I can support regardless of party.
This feels credible.
This feels hopeful.
I want to be part of this.
Use the survey results, the research findings, the principles, the storytelling, or any other elements you believe will help build trust and inspire participation.
Don't just impress us with flashy visuals. Impress us with a website experience that inspires people to become part of the movement and cast their vote.
The final call-to-action should feel like the natural conclusion of the journey, not a request for engagement.
Our goal is not simply to inform visitors. Our goal is to inspire them to cast their vote.
Prioritize emotional impact, storytelling, clarity, and persuasion over decorative design elements.
Final words:
Design a website experience that successfully inspires visitors to take the survey and cast their vote.
Think like a storyteller, not just a designer.
Thank you for your interest in the project.
Best of luck.

```html
<!DOCTYPE html>
<html lang="en">
<head>
<meta charset="utf-8">
<title>Lantern Square. Steady Course. — Website Design</title>
<link href="https://fonts.googleapis.com/css2?family=Libre+Caslon+Text:ital,wght@0,400;0,700;1,400&family=Inter:wght@400;500;600;700&family=Oswald:ital,wght@0,600;1,600&display=swap" rel="stylesheet">
<style>
:root{
  --backdrop:#e8e8e8;
  --orange:#e8731a;
  --orange-soft:#f4a866;
  --cream:#f3e8d8;
  --ink:#1d1a17;
  --dark:#1c1816;
  --gold:#ecc47e;
  --white:#ffffff;
  --serif:"Libre Caslon Text",Georgia,serif;
  --sans:"Inter",Arial,sans-serif;
}
*{box-sizing:border-box;margin:0;padding:0}
html,body{width:925px;height:1200px;overflow:hidden;background:var(--backdrop)}
.canvas{position:relative;width:925px;height:1200px;overflow:hidden;background:var(--backdrop)}
.stage{position:absolute;left:0;top:0;width:1684px;height:2184px;transform:scale(.5493);transform-origin:0 0;font-family:var(--sans);color:var(--ink)}
.abs{position:absolute}
.serif{font-family:var(--serif)}
.accent{color:var(--orange)}
.label{position:absolute;font-size:7px;font-weight:600;letter-spacing:.3px;color:var(--orange);text-transform:uppercase}
.btn{position:absolute;display:flex;align-items:center;justify-content:center;font-size:7.5px;font-weight:500}
.btn-orange{background:var(--orange);color:var(--white);box-shadow:0 0 0 2px #fff inset}
.btn-light{background:var(--white);color:var(--ink);border:2px solid #bbb}
.btn-ghost{background:rgba(255,255,255,.12);color:var(--white);border:2px solid #ccc}
.photo{position:absolute}
.outline-word{position:absolute;font-family:var(--serif);color:transparent;-webkit-text-stroke:1.4px var(--orange-soft);white-space:nowrap;line-height:1}
.outline-word.vertical{text-align:center;transform-origin:center}
.rule{position:absolute;background:var(--orange-soft)}
.body-sm{position:absolute;font-size:8.5px;line-height:1.45;color:#4a423b}

.page-left{left:99px;top:91px;width:709px;height:2001px;background:var(--cream)}
.hero{left:99px;top:91px;width:709px;height:400px;background:linear-gradient(180deg,#4a4340 0%,#6d6257 45%,#3f3935 100%)}
.nav-brand{left:158px;top:100px;font-family:var(--serif);font-size:11px;color:var(--gold)}
.nav-links{left:406px;top:103px;display:flex;gap:9px;font-size:6px;color:#fff}
.nav-links span:first-child{color:var(--gold)}
.hero-title{position:absolute;left:150px;width:607px;top:216px;text-align:center;font-family:var(--serif);font-weight:400;font-size:31px;line-height:35px;color:#fff}
.hero-sub{left:150px;width:607px;top:291px;text-align:center;font-family:var(--serif);font-style:italic;font-size:8.5px;color:#f1eae0}
.video{left:160px;top:362px;width:589px;height:286px;background:linear-gradient(120deg,#d9b27a 0%,#e9c58c 35%,#9a5d3a 65%,#5a4a52 100%);border:1.5px solid #f6dcb8}
.video-caption{left:170px;top:620px;font-family:"Oswald",var(--sans);font-style:italic;font-weight:600;font-size:22px;color:#fff;letter-spacing:.2px}
.mission h2,.who h2{font-family:var(--serif);font-weight:400;color:var(--ink)}
.who-section{left:99px;top:968px;width:709px;height:347px;background:var(--white)}
.journey{left:99px;top:1314px;width:709px;height:344px;background:linear-gradient(180deg,#2b2624 0%,#141110 100%)}
.principles-card{position:absolute;background:var(--white);box-shadow:0 1px 4px rgba(0,0,0,.08);padding:0 8px}
.principles-card .num{position:absolute;right:8px;top:10px;font-size:9px;font-style:italic;color:var(--ink)}
.principles-card .corner{position:absolute;left:0;top:0;width:0;height:0;border-top:10px solid var(--orange);border-right:10px solid transparent}
.principles-card h4{font-family:var(--serif);font-weight:400;font-size:9.5px;line-height:1.2;color:var(--ink);margin-bottom:3px}
.principles-card p{font-size:7px;line-height:1.4;color:#5a524b}
.principles-card .icon{margin-bottom:6px}

.page-right{left:876px;top:91px;width:708px;height:1480px;background:var(--white)}
.survey-photo{left:955px;top:212px;width:551px;height:280px;background:linear-gradient(90deg,#2b221d 0%,#4a3d33 45%,#8a7563 100%)}
.card-yes{left:912px;top:621px;width:307px;height:211px;background:var(--cream);border:1.5px solid var(--orange-soft)}
.card-chart{left:1231px;top:621px;width:306px;height:211px;background:var(--dark)}
.bullets{position:absolute;left:932px;top:688px;width:270px;list-style:none;font-size:8px;line-height:1.5;color:#3a332d}
.bullets li{position:relative;padding-left:12px;margin-bottom:7px}
.bullets li::before{content:"";position:absolute;left:0;top:3px;border-left:5px solid var(--orange);border-top:3px solid transparent;border-bottom:3px solid transparent}
.history{left:876px;top:890px;width:364px;height:293px;background:var(--gold)}
.footer{left:876px;top:1388px;width:708px;height:183px;background:var(--dark)}
.footer h5{position:absolute;font-size:7.5px;font-weight:600;color:#fff}
.footer .list{position:absolute;font-size:6.3px;line-height:1.55;color:#bdb4aa}
</style>
</head>
<body>
<div class="canvas">
<div class="stage">

  <div class="abs page-left"></div>

  <section class="abs hero" role="img" aria-label="Sepia collage of a historic president's portrait, a waving flag and a young girl smiling"></section>
  <div class="abs nav-brand">Lantern Square. Steady Course.</div>
  <nav class="abs nav-links"><span>Home</span><span>Mission</span><span>Who We Are</span><span>Our Journey</span><span>Seven Principles</span><span>Survey Results</span></nav>
  <div class="btn btn-light" style="left:690px;top:97px;width:58px;height:20px;font-size:6px">Vote YES Now</div>
  <div class="abs" style="left:99px;top:121px;width:709px;height:1px;background:rgba(255,255,255,.35)"></div>
  <div class="abs" style="left:440px;top:205px;font-size:8px;color:#fff;letter-spacing:1px">★★★</div>
  <h1 class="hero-title">A <span class="accent">Government</span> Legally<br>Required to Serve the People</h1>
  <div class="abs hero-sub">Government should be honest, transparent, and accountable to the people it serves.</div>
  <div class="btn btn-light" style="left:369px;top:315px;width:67px;height:25px">Vote YES Now</div>
  <div class="btn btn-ghost" style="left:449px;top:315px;width:90px;height:25px">Learn the Principles</div>

  <div class="abs video" role="img" aria-label="Video still: a woman holding a flag at sunset beside a statue and soldiers"></div>
  <svg class="abs" style="left:438px;top:488px" width="32" height="32" viewBox="0 0 32 32"><circle cx="16" cy="16" r="14.5" fill="#1b1715" stroke="#fff" stroke-width="2"/><path d="M13 10.5 L22 16 L13 21.5Z" fill="#fff"/></svg>
  <div class="abs video-caption">1016 PEOPLE ALREADY VOTED YES FOR THE BALLOT</div>

  <div class="rule" style="left:158px;top:648px;width:1px;height:320px"></div>
  <div class="rule" style="left:748px;top:648px;width:1px;height:320px"></div>
  <div class="outline-word vertical" style="left:40px;top:782px;width:200px;font-size:46px;transform:rotate(-90deg)">MISSION</div>
  <div class="photo" style="left:185px;top:686px;width:246px;height:245px;background:linear-gradient(135deg,#6f8aa6 0%,#3e4d63 60%,#2a3140 100%)" role="img" aria-label="Historic photo of a president speaking at a microphone"></div>
  <div class="label" style="left:456px;top:704px">Mission Statement</div>
  <div class="abs mission" style="left:455px;top:726px">
    <h2 style="font-size:29px;line-height:33px"><span class="accent">Why</span> We</h2>
    <h2 style="font-size:23px;line-height:30px">Started This Movement</h2>
  </div>
  <p class="body-sm" style="left:456px;top:796px;width:240px">Today, not a single law binds our government to act honestly, and in our best interest.<br>If our government exists solely to serve us,</p>
  <div class="abs serif" style="left:456px;top:838px;font-size:12.5px;color:var(--ink)">Why isn’t it legally required to?</div>
  <p class="body-sm" style="left:456px;top:858px">We founded this movement to change that.</p>
  <div class="btn btn-orange" style="left:456px;top:887px;width:63px;height:26px">Learn More</div>

  <section class="abs who-section"></section>
  <div class="label" style="left:186px;top:1007px">Who We Are</div>
  <div class="abs who" style="left:185px;top:1030px">
    <h2 style="font-size:23px;line-height:28px">Together for Honest</h2>
    <h2 style="font-size:28px;line-height:30px;color:var(--orange)">Government</h2>
  </div>
  <p class="body-sm" style="left:186px;top:1099px;width:255px">We are a bipartisan movement based in Washington, D.C. We believe Americans deserve a government legally required to act honestly, transparently, and in the public’s best interest.</p>
  <div class="abs" style="left:186px;top:1154px;width:2px;height:56px;background:var(--orange)"></div>
  <p class="body-sm" style="left:191px;top:1153px;width:225px">At a time of growing division and distrust, we are working to unite Americans around a simple idea:</p>
  <p class="body-sm" style="left:191px;top:1183px;width:225px;color:var(--ink);font-weight:600">Government should faithfully serve the people, not special interests.</p>
  <div class="btn btn-orange" style="left:186px;top:1224px;width:63px;height:26px">Explore Us</div>
  <div class="abs" style="left:463px;top:998px;width:273px;height:255px;border:1px solid var(--orange-soft)"></div>
  <div class="photo" style="left:457px;top:1006px;width:271px;height:259px;background:linear-gradient(160deg,#8aa0a8 0%,#53605f 50%,#2d3330 100%)" role="img" aria-label="Historic photo of a civil rights leader waving to a vast crowd"></div>
  <div class="outline-word" style="left:418px;top:1232px;font-size:44px">WHO</div>
  <div class="abs" style="left:755px;top:1244px;width:5px;height:5px;background:#ccc"></div>

  <section class="abs journey" role="img" aria-label="Dark background photo of marchers holding protest placards"></section>
  <div class="label" style="left:426px;top:1351px">Our Journey</div>
  <div class="abs serif" style="left:99px;width:709px;top:1364px;text-align:center;font-size:27px;color:#fff">The <span class="accent">Journey</span> to This Moment</div>
  <div class="outline-word" style="left:410px;top:1430px;font-size:40px;-webkit-text-stroke:1px rgba(255,255,255,.35)">MAR &nbsp; &nbsp; &nbsp; 2026</div>
  <div class="abs" style="left:183px;top:1466px;width:543px;height:2px;background:#fff"></div>
  <svg class="abs" style="left:175px;top:1459px" width="560" height="16"><g fill="#1a1614" stroke="#fff" stroke-width="2"><circle cx="8" cy="8" r="5"/><circle cx="158" cy="8" r="5"/><circle cx="551" cy="8" r="5"/></g></svg>
  <div class="abs" style="left:492px;top:1421px;width:92px;height:92px;border-radius:50%;border:3px solid var(--orange);background:linear-gradient(135deg,#8b7d72,#3c332d)" role="img" aria-label="Portrait of a president speaking"></div>
  <div class="abs" style="left:158px;top:1445px;font-size:8px;color:var(--orange)">August 2024</div>
  <div class="abs" style="left:308px;top:1445px;font-size:8px;color:var(--orange)">October 2025</div>
  <div class="abs" style="left:706px;top:1445px;font-size:8px;color:var(--orange)">April 2026</div>
  <div class="abs" style="left:140px;top:1479px;width:86px;text-align:center;font-size:6px;line-height:1.5;color:#cfc6bd">Started a nonprofit with a simple goal:<br><b style="color:#fff">Americans deserve an honest government.</b></div>
  <div class="abs" style="left:288px;top:1479px;width:90px;text-align:center;font-size:6px;line-height:1.5;color:#cfc6bd">Identified core principles that Americans broadly agree government should uphold.</div>
  <div class="abs" style="left:688px;top:1479px;width:76px;text-align:center;font-size:6px;line-height:1.5;color:#cfc6bd">Conducted a national pre-registered study with Americans across the political spectrum.</div>
  <div class="abs" style="left:488px;top:1521px;width:100px;text-align:center;font-size:7.5px;color:var(--orange)">March 2026</div>
  <div class="abs" style="left:488px;top:1533px;width:100px;text-align:center;font-size:6px;line-height:1.5;color:#cfc6bd">Turned those principles into a rigorous framework:<br><b style="color:#fff">Lantern Square. Steady Course.</b></div>
  <div class="abs serif" style="left:99px;width:709px;top:1588px;text-align:center;font-size:70px;font-weight:700;letter-spacing:2px;line-height:1;background:linear-gradient(180deg,#5a5552 0%,#1b1816 90%);-webkit-background-clip:text;background-clip:text;color:transparent">OUR JOURNEY</div>

  <div class="rule" style="left:158px;top:1657px;width:1px;height:435px"></div>
  <div class="rule" style="left:748px;top:1657px;width:1px;height:435px"></div>
  <div class="label" style="left:99px;width:709px;text-align:center;top:1694px">Our Principles</div>
  <div class="abs serif" style="left:99px;width:709px;top:1708px;text-align:center;font-size:27px">The <span class="accent">Seven</span> Principles</div>
  <div class="abs" style="left:99px;width:709px;top:1747px;text-align:center;font-size:8.5px;color:#4a423b">A framework built around values most Americans already agree on.</div>
  <div class="outline-word vertical" style="left:602px;top:1852px;width:330px;font-size:46px;transform:rotate(90deg)">PRINCIPLES</div>

  <div class="principles-card" style="left:179px;top:1770px;width:171px;height:235px">
    <div class="photo" style="left:5px;top:6px;width:161px;height:144px;background:linear-gradient(180deg,#6b5d52 0%,#9a3b24 55%,#3b332d 100%)" role="img" aria-label="Historic photo of a crowd marching behind a banner"></div>
    <div class="num" style="top:16px;color:#fff">01</div>
    <div style="position:absolute;left:10px;top:160px">
      <svg class="icon" width="18" height="18" viewBox="0 0 18 18" fill="none" stroke="#e8731a" stroke-width="1.2"><circle cx="9" cy="7" r="4"/><path d="M3 16c1-3 3.5-4.5 6-4.5s5 1.5 6 4.5"/></svg>
      <h4 style="color:var(--orange)">Serve the Public Good</h4>
      <p style="width:150px">Public officials should only serve the public good, not private interests.</p>
    </div>
  </div>

  <div class="principles-card" style="left:358px;top:1770px;width:120px;height:125px">
    <span class="corner"></span><span class="num">02</span>
    <div style="position:absolute;left:8px;top:42px;width:106px">
      <svg class="icon" width="18" height="18" viewBox="0 0 18 18" fill="none" stroke="#e8731a" stroke-width="1.2"><rect x="4" y="2" width="11" height="14"/><path d="M7 6h5M7 9h5M7 12h3"/></svg>
      <h4>Truth &amp; Evidence</h4><p>Major government decisions should be based on truth and rigorous evidence.</p>
    </div>
  </div>
  <div class="principles-card" style="left:484px;top:1770px;width:120px;height:100px">
    <span class="corner"></span><span class="num">03</span>
    <div style="position:absolute;left:8px;top:18px;width:106px">
      <svg class="icon" width="18" height="18" viewBox="0 0 18 18" fill="none" stroke="#e8731a" stroke-width="1.2"><rect x="2" y="3" width="10" height="10"/><rect x="6" y="6" width="10" height="10"/></svg>
      <h4>Transparent Reasoning</h4><p>People should be able to clearly see the reasoning behind public decisions.</p>
    </div>
  </div>
  <div class="principles-card" style="left:610px;top:1770px;width:119px;height:125px">
    <span class="corner"></span><span class="num">04</span>
    <div style="position:absolute;left:8px;top:28px;width:106px">
      <svg class="icon" width="18" height="18" viewBox="0 0 18 18" fill="none" stroke="#e8731a" stroke-width="1.2"><path d="M9 2l6 3v4c0 4-3 6-6 7-3-1-6-3-6-7V5z"/><path d="M6 9l2 2 4-4"/></svg>
      <h4>Meaningful Accountability</h4><p>Citizens should have a way to challenge flawed reasoning and receive a real response.</p>
    </div>
  </div>
  <div class="principles-card" style="left:484px;top:1878px;width:120px;height:127px">
    <span class="corner"></span><span class="num">06</span>
    <div style="position:absolute;left:8px;top:32px;width:106px">
      <svg class="icon" width="18" height="18" viewBox="0 0 18 18" fill="none" stroke="#e8731a" stroke-width="1.2"><path d="M9 2L17 16H1z"/><path d="M9 7v4M9 13v1"/></svg>
      <h4>Consequences for Misleading</h4><p>Lying or misleading the public in official decisions should carry real consequences.</p>
    </div>
  </div>
  <div class="principles-card" style="left:358px;top:1903px;width:120px;height:102px">
    <span class="corner"></span><span class="num">05</span>
    <div style="position:absolute;left:8px;top:18px;width:106px">
      <svg class="icon" width="18" height="18" viewBox="0 0 18 18" fill="none" stroke="#e8731a" stroke-width="1.2"><path d="M3 15l6-6M9 9l3-6 3 3-6 3"/><circle cx="4" cy="4" r="2"/></svg>
      <h4>Conflict Disclosure</h4><p>Conflicts of interest should be disclosed before decisions are made.</p>
    </div>
  </div>
  <div class="principles-card" style="left:610px;top:1903px;width:119px;height:102px">
    <span class="corner"></span><span class="num">07</span>
    <div style="position:absolute;left:8px;top:22px;width:106px">
      <svg class="icon" width="18" height="18" viewBox="0 0 18 18" fill="none" stroke="#e8731a" stroke-width="1.2"><ellipse cx="6" cy="6" rx="4" ry="2"/><path d="M2 6v4c0 1 2 2 4 2s4-1 4-2V6"/><circle cx="13" cy="11" r="3.5"/></svg>
      <h4>People Over Money</h4><p>Money should never outweigh people’s voice.</p>
    </div>
  </div>

  <div class="abs" style="left:175px;top:2016px;width:554px;height:40px;border:1px solid var(--orange-soft)"></div>
  <div class="abs" style="left:179px;top:2020px;width:550px;height:32px;background:linear-gradient(90deg,#2a2522 70%,#3d3633 100%);display:flex;align-items:center;color:#fff">
    <svg style="margin-left:12px" width="18" height="16" viewBox="0 0 18 16" fill="none" stroke="#fff" stroke-width="1"><path d="M9 1v14M3 15h12M2 4h14M4 4L1 10h6zM14 4l-3 6h6z"/></svg>
    <span style="margin-left:17px;font-size:13px;font-weight:600">89.9%</span>
    <span class="serif" style="margin-left:6px;font-size:9px">Agreed</span>
    <span style="margin-left:13px;width:1px;height:20px;background:#aaa"></span>
    <span class="serif" style="margin-left:14px;font-size:7.5px">of Americans agreed with these seven principles.</span>
  </div>

  <div class="abs page-right"></div>
  <div class="label" style="left:876px;width:708px;text-align:center;top:127px">The Survey</div>
  <div class="abs serif" style="left:876px;width:708px;top:140px;text-align:center;font-size:25px">What <span class="accent" style="font-size:29px">Americans</span> Told Us</div>
  <div class="abs" style="left:876px;width:708px;top:181px;text-align:center;font-size:8.5px;color:#4a423b">Would vote YES for a legal framework built around these principles.</div>

  <div class="outline-word vertical" style="left:837px;top:325px;width:200px;font-size:46px;transform:rotate(-90deg)">SURVEY</div>
  <div class="abs survey-photo" role="img" aria-label="Sepia photo of a city skyline of skyscrapers"></div>
  <div class="abs" style="left:965px;top:205px;width:215px;height:255px;border:1px solid var(--orange-soft)"></div>
  <div class="abs" style="left:980px;top:233px;font-size:22px;color:#fff">82.9%*</div>
  <div class="abs" style="left:980px;top:263px;width:180px;font-size:9px;line-height:1.4;color:#fff">of Americans said, YES on a state ballot vote.</div>
  <div class="abs" style="left:966px;top:296px;width:181px;height:17px;background:var(--orange);color:#fff;font-size:7px;display:flex;align-items:center;padding-left:14px">(*actual numbers will be disclosed later)</div>
  <div class="abs" style="left:980px;top:327px;width:175px;font-size:8.5px;line-height:1.45;color:#fff">We conducted a pre-registered national study with X number Americans across the political spectrum.</div>
  <div class="abs serif" style="left:966px;top:415px;font-size:16px;color:#fff">We first laid out the 7 principles. We asked if they agree?</div>
  <div class="abs" style="left:966px;top:450px;width:24px;height:1px;background:var(--orange)"></div>
  <div class="abs" style="left:996px;top:445px;font-size:9px;color:#fff">89.9%* said they Agree.</div>

  <div class="label" style="left:876px;width:708px;text-align:center;top:531px">Then We Asked:</div>
  <div class="abs serif" style="left:876px;width:708px;top:547px;text-align:center;font-size:22px;line-height:30px">Would you support a legal<br><span class="accent" style="font-size:27px">framework</span> built around them?</div>

  <div class="abs card-yes"></div>
  <div class="abs" style="left:912px;top:633px;width:154px;height:30px;background:var(--orange);color:#fff;display:flex;align-items:center;padding-left:10px">
    <svg width="14" height="12" viewBox="0 0 14 12" fill="none" stroke="#fff" stroke-width="1.6"><path d="M1 6l4 4 8-9"/></svg>
    <span style="margin-left:8px;font-size:17px;font-weight:500">82.9%*</span><span class="serif" style="margin-left:6px;font-size:9px">said yes</span>
  </div>
  <ul class="bullets">
    <li><b>14.4%*</b> remained neutral. Only <b>2.7%*</b> actively opposed it.</li>
    <li>But broad support is easy when ideas stay vague.<br>So we stress-tested it.</li>
    <li>But broad support is easy when ideas stay vague.<br>So we stress-tested it.</li>
    <li>We showed participants the full framework. The legal structure. The enforcement model.<br>The actual mechanism.</li>
  </ul>

  <div class="abs card-chart"></div>
  <div class="abs serif" style="left:1246px;top:637px;font-size:10.5px;color:#fff">Most reforms lose support once the details appear.</div>
  <div class="abs" style="left:1246px;top:655px;font-size:8px;color:#cfc6bd">This one didn’t. Support held.</div>
  <svg class="abs" style="left:1246px;top:676px" width="280" height="120" viewBox="0 0 280 120">
    <line x1="4" y1="2" x2="4" y2="102" stroke="#fff" stroke-width="1"/>
    <line x1="4" y1="102" x2="276" y2="102" stroke="#fff" stroke-width="1"/>
    <g font-family="Inter,Arial,sans-serif" font-size="6" fill="#fff">
      <text x="9" y="10">Democrats</text><text x="9" y="43">Republicans</text><text x="9" y="76">Independants</text>
    </g>
    <rect x="9" y="14" width="251" height="13" fill="#fff"/><rect x="9" y="14" width="226" height="13" fill="#f07a1f"/>
    <rect x="9" y="47" width="251" height="13" fill="#fff"/><rect x="9" y="47" width="208" height="13" fill="#f28f45"/>
    <rect x="9" y="80" width="251" height="13" fill="#fff"/><rect x="9" y="80" width="197" height="13" fill="#f6b47c"/>
    <g stroke="#e8731a" stroke-width="1"><line x1="19" y1="99" x2="19" y2="105"/><line x1="79" y1="99" x2="79" y2="105"/><line x1="139" y1="99" x2="139" y2="105"/><line x1="199" y1="99" x2="199" y2="105"/><line x1="260" y1="99" x2="260" y2="105"/></g>
    <g font-family="Inter,Arial,sans-serif" font-size="6" fill="#e8731a" text-anchor="middle"><text x="19" y="115">0</text><text x="79" y="115">25</text><text x="139" y="115">50</text><text x="199" y="115">75</text><text x="260" y="115">100</text></g>
  </svg>
  <div class="abs" style="left:1246px;top:805px;font-size:9px;font-weight:500;color:#fff">They all said, YES.</div>

  <div class="abs" style="left:1227px;top:879px;width:348px;height:1px;background:var(--orange-soft)"></div>
  <section class="abs history"></section>
  <div class="abs" style="left:1010px;top:1100px;width:220px;height:83px;background:linear-gradient(180deg,rgba(232,170,70,0) 0%,rgba(232,170,70,.45) 100%)" role="img" aria-label="Faint silhouette of a city skyline with the Statue of Liberty"></div>
  <div class="photo" style="left:1240px;top:890px;width:344px;height:293px;background:linear-gradient(160deg,#d9d3c9 0%,#9c8e7d 45%,#4a3f36 100%)" role="img" aria-label="Sepia photo of marchers in front of the Capitol dome"></div>
  <div class="abs serif" style="left:911px;top:944px;font-size:33px">Be Part of <span class="accent" style="font-size:36px">History</span></div>
  <div class="abs" style="left:912px;top:991px;font-size:8.5px;color:#4a3e30">For decades, we have argued over policies, parties, and ideologies.</div>
  <div class="abs" style="left:912px;top:1009px;width:280px;font-size:8.5px;line-height:1.45;color:#4a3e30">Today, across political lines, generations, and races, Americans are arriving at the same conclusion:<br><span style="color:var(--ink)">We deserve a government legally required to serve the people honestly.</span></div>
  <div class="abs" style="left:912px;top:1067px;font-size:8.5px;color:var(--orange)">And we don’t have to ask for it. We just have to vote for it.</div>
  <div class="btn btn-light" style="left:913px;top:1093px;width:66px;height:25px;border-color:#fff">Vote Now</div>

  <div class="abs" style="left:876px;top:1183px;width:708px;height:205px;background:var(--dark)"></div>
  <div class="photo" style="left:876px;top:1202px;width:208px;height:186px;background:linear-gradient(150deg,#cbbfae,#6d5d4f)" role="img" aria-label="Sepia photo of a suffragist pointing toward a crowd"></div>
  <div class="photo" style="left:1100px;top:1202px;width:204px;height:186px;background:linear-gradient(150deg,#8d7a68,#3a2e26)" role="img" aria-label="Sepia portrait of an early women's rights leader"></div>
  <div class="photo" style="left:1320px;top:1202px;width:264px;height:186px;background:linear-gradient(150deg,#e4ddd3,#9a8c7e)" role="img" aria-label="Sepia photo of a suffragist raising a banner with stars"></div>

  <footer class="abs footer">
    <div class="abs" style="left:36px;top:22px;width:625px;height:1px;background:rgba(232,115,26,.5)"></div>
    <div class="abs" style="left:244px;top:22px;width:1px;height:140px;background:rgba(232,115,26,.5)"></div>
    <div class="abs" style="left:349px;top:22px;width:1px;height:140px;background:rgba(232,115,26,.5)"></div>
    <div class="abs" style="left:521px;top:22px;width:1px;height:140px;background:rgba(232,115,26,.5)"></div>
    <div class="abs serif" style="left:36px;top:50px;font-size:11px;color:var(--gold)">Lantern Square. Steady Course.</div>
    <div class="list" style="left:36px;top:69px;width:190px">A bipartisan movement dedicated to creating a government that is legally required to act honestly, transparently, and in the public’s best interest.</div>
    <svg class="abs" style="left:35px;top:106px" width="52" height="14"><g fill="none" stroke="#fff" stroke-width="1"><circle cx="7" cy="7" r="6"/><circle cx="26" cy="7" r="6"/><circle cx="45" cy="7" r="6"/></g></svg>
    <h5 style="left:269px;top:48px">Quick Link</h5>
    <div class="list" style="left:269px;top:64px">Home<br>Mission<br>Who We Are<br>Our Journey<br>Seven Principles<br>Survey Results</div>
    <h5 style="left:373px;top:48px">Contact Us</h5>
    <svg class="abs" style="left:373px;top:68px" width="12" height="48"><g fill="none" stroke="#fff" stroke-width="1"><circle cx="6" cy="6" r="5.5"/><circle cx="6" cy="24" r="5.5"/><circle cx="6" cy="42" r="5.5"/></g><path d="M6 3.2a2 2 0 0 1 2 2c0 1.5-2 3.6-2 3.6s-2-2.1-2-3.6a2 2 0 0 1 2-2z" fill="#fff"/><rect x="3" y="22" width="6" height="4" fill="none" stroke="#fff" stroke-width=".7"/><circle cx="6" cy="42" r="2.6" fill="none" stroke="#fff" stroke-width=".7"/></svg>
    <div class="list" style="left:391px;top:71px">Washington, D.C., United States</div>
    <div class="list" style="left:391px;top:89px;color:var(--orange);text-decoration:underline">info@lanternsquare.org</div>
    <div class="list" style="left:391px;top:107px">lanternsquare.org</div>
    <h5 style="left:546px;top:48px">Stay Informed</h5>
    <div class="list" style="left:546px;top:66px;width:110px">Receive updates and important announcements.</div>
    <div class="abs" style="left:546px;top:92px;width:115px;height:18px;background:#2e2926;border:1px solid #4a423d;font-size:6.3px;color:#bdb4aa;display:flex;align-items:center;padding-left:5px">Enter Your Email</div>
    <div class="btn btn-orange" style="left:546px;top:122px;width:59px;height:20px;font-size:7px">Subscribe</div>
    <div class="abs" style="left:0;top:162px;width:708px;height:1px;background:rgba(232,115,26,.6)"></div>
    <div class="list" style="left:36px;top:168px;color:#fff">© 2026 Lantern Square. Steady Course. All Rights Reserved.</div>
    <div class="list" style="left:572px;top:168px;color:#fff">Privacy Policy | Terms of Use</div>
  </footer>

</div>
</div>
</body>
</html>
```